African homeware retailer needs a web page design

We need a web page design for a new homeware and accessories store based in Johannesburg, South Africa. Our store carries modern African inspired items from designers that support social development and poverty alleviation initiatives. We have a particular preference for outfits that are centred on the empowerment of women.

Our business celebrates the skill, design and product of African craft and the work of designers looking to take that forward in a socially beneficial way (creating employment, developing skills, supporting local crafts people etc). We aim to carry items and inspirations from all over the African continent.

We would like to see a design that communicates African beauty and elegance without the typical tribal references that are made in reference to African craft or art.

We would like the web page to be stylish, uncomplicated, modern, captivating and appealing to the discerning customer. A similar value proposition is that of http://www.lanterwickhouse.example/.

This is an e-commerce website which must be attractive to both individual buyers and design professionals so the website needs to look professional.

Here are links to some websites we like:
http://www.corvellinteriors.example/
http://www.tmerrow.example/

Our logo is attached to the brief.

Target Market(s)

Our target market is female, age 20-50. However should not alienate the design conscious male customer therefore

Industry/Entity Type

E-Commerce

Requirements
Must have
• - A featured product banner which includes a photograph and text. This should be easy to edit as we will be changing the featured product regularly
- An easily expendable products section with categories. Examples of categories could be cushions, bedding, crockery etc. Should be easy to add new categories as well as new product pictures
- Home/landing page should be uncluttered
- Should use the logo and should be easy to change the logo which we have in various colour combinations. We plan to change the logo colours depending on circumstance e.g. make it red and white around Valentines day (similar to the way Quorbit frequently changes the logo on their landing page)

```html
<!DOCTYPE html>
<html lang="en">
<head>
<meta charset="utf-8">
<title>Sahel Grace – Homeware &amp; Accessories</title>
<link href="https://fonts.googleapis.com/css2?family=Fira+Sans:wght@500;600&family=Open+Sans:wght@300;400;600&display=swap" rel="stylesheet">
<style>
:root{
  --page-bg:#fbf3c9;
  --footer-bg:#f7ecbb;
  --green:#3f9a4a;
  --green-dark:#2f7f39;
  --green-light:#5bb163;
  --ink:#3d3d3a;
  --muted:#5a5a55;
  --overlay:rgba(70,70,70,.88);
  --field:#fffbe6;
  --search:#f7edc0;
}
*{box-sizing:border-box;margin:0;padding:0}
html,body{width:1200px;height:1179px;overflow:hidden;background:var(--page-bg)}
body{font-family:"Open Sans",sans-serif;color:var(--ink)}
.page{position:relative;width:1140px;height:1120px;transform:scale(1.0526);transform-origin:0 0}
.abs{position:absolute}

/* header */
.brand{left:510px;top:14px;width:120px;text-align:center;color:var(--green-dark)}
.brand-square{width:30px;height:30px;margin:0 auto 8px;background:var(--green-dark)}
.brand-name{font-family:"Fira Sans",sans-serif;font-weight:600;font-size:15px;letter-spacing:1.5px;line-height:1.1;text-transform:uppercase}
.brand-tag{font-size:5px;letter-spacing:.5px;color:var(--green-dark);margin-top:2px}
.account{right:100px;top:13px;font-family:"Fira Sans",sans-serif;font-weight:600;font-size:14px;color:var(--green)}
.account span{margin:0 8px}
.cart{right:103px;top:53px;font-size:14px;font-weight:300;color:var(--muted);display:flex;align-items:center;gap:5px}
.search{left:794px;top:85px;width:246px;height:26px;background:var(--search);border-radius:2px;font-size:8px;color:#b9b08a;padding:8px 8px;display:flex;justify-content:space-between;align-items:center}

/* navigation */
.nav{left:100px;top:121px;width:940px;height:58px;display:flex;background:linear-gradient(#5cae62,var(--green-dark))}
.nav a{display:flex;align-items:center;justify-content:center;height:100%;border-right:1px solid rgba(255,255,255,.25);color:#fff;text-decoration:none;font-family:"Fira Sans",sans-serif;font-weight:600;font-size:14px}
.nav a:last-child{border-right:0}

/* hero */
.hero{left:100px;top:179px;width:940px;height:362px;background:
  radial-gradient(ellipse 180px 90px at 680px 260px,#f4f2ec 0,transparent 70%),
  radial-gradient(ellipse 260px 140px at 300px 180px,#b9ada0 0,transparent 75%),
  linear-gradient(90deg,#d9cdb8 0,#a88a66 30%,#b7a287 55%,#e8e4db 75%,#f1efe9 100%)}
.dots{left:535px;top:512px;display:flex;gap:6px}
.dots i{width:14px;height:14px;border-radius:50%;background:#fff;display:block}
.dots i.on{background:var(--green)}

/* promo tiles */
.promo{top:570px;width:300px;height:173px}
.promo-1{left:100px;background:linear-gradient(120deg,#d94b6a,#e9d27a 45%,#c8c0b0)}
.promo-2{left:421px;background:radial-gradient(ellipse 70px 40px at 80px 90px,#8a5a44,transparent 80%),#ffffff}
.promo-3{left:740px;background:linear-gradient(90deg,#e8e6e2,#c9a98a 55%,#efece6)}
.promo-card{position:absolute;left:115px;top:34px;width:178px;height:116px;background:var(--overlay);color:#fff;text-align:center}
.promo-title{font-family:"Fira Sans",sans-serif;font-weight:600;font-size:19px;margin-top:16px}
.promo-offer{font-weight:300;font-size:29px;line-height:1;margin-top:3px;text-transform:uppercase}
.promo-btn{display:inline-block;margin-top:9px;background:var(--green);font-family:"Fira Sans",sans-serif;font-weight:600;font-size:14px;padding:3px 6px}

/* footer */
.footer{left:0;top:773px;width:1140px;height:347px;background:var(--footer-bg)}
.f-head{font-family:"Fira Sans",sans-serif;font-weight:600;font-size:14px;color:var(--ink)}
.newsletter{left:100px;top:810px}
.signup{left:100px;top:836px;width:340px;height:50px;background:var(--field);font-size:13px;color:#c8c2a4;padding:17px 7px}
.signup-go{position:absolute;left:277px;top:5px;width:55px;height:40px;background:var(--green);color:#fff;font-family:"Fira Sans",sans-serif;font-weight:600;font-size:14px;display:flex;align-items:center;justify-content:center}
.blurb{left:100px;top:894px;width:350px;font-size:13.5px;line-height:28px;color:var(--ink)}
.cards{left:105px;top:956px;display:flex;gap:6px}
.cards span{height:25px;border:1px solid #cfc8a8;background:#fff;font-family:"Fira Sans",sans-serif;font-weight:600;font-size:10px;color:var(--ink);display:flex;align-items:center;justify-content:center}
.col{top:810px}
.col ul{list-style:none;margin-top:17px}
.col li{font-size:13.5px;line-height:28px;color:var(--ink)}
.col-links{left:493px}
.col-stories{left:673px}
.col-social{left:843px;width:197px}
.col-social li{display:flex;justify-content:space-between;align-items:center}
.col-social li i{width:22px;height:22px;border-radius:50%;background:var(--green);display:block}
.copy{left:0;top:1073px;width:1140px;text-align:center;font-size:13px;color:var(--muted)}
</style>
</head>
<body>
<div class="page">

  <header>
    <div class="abs brand">
      <div class="brand-square"></div>
      <div class="brand-name">Sahel Grace</div>
      <div class="brand-tag">homeware · accessories</div>
    </div>
    <div class="abs account">Sign in<span>|</span>My Account</div>
    <div class="abs cart">
      <svg width="19" height="16" viewBox="0 0 19 16" fill="none" stroke="#6a6a62" stroke-width="1.3"><path d="M1 1h3l2 9h10l2-7H5"/><circle cx="7.5" cy="13.5" r="1.4"/><circle cx="14.5" cy="13.5" r="1.4"/></svg>
      Add to cart :&nbsp; $0.00
    </div>
    <div class="abs search">Type search
      <svg width="11" height="11" viewBox="0 0 11 11" fill="none" stroke="#8a8470" stroke-width="1.3"><circle cx="4.5" cy="4.5" r="3.3"/><path d="M7 7l3.3 3.3"/></svg>
    </div>
  </header>

  <nav class="abs nav">
    <a style="width:118px">Furniture</a>
    <a style="width:93px">Decor</a>
    <a style="width:116px">About us</a>
    <a style="width:116px">Products</a>
    <a style="width:152px">Upcoming sale</a>
    <a style="width:90px">Faqs</a>
    <a style="width:140px">New Arrivals</a>
    <a style="width:115px">Contact</a>
  </nav>

  <section class="abs hero" role="img" aria-label="Featured product photo: patterned cushions on a tan sofa beside a glass lamp and white flowers"></section>
  <div class="abs dots"><i class="on"></i><i></i><i></i><i></i></div>

  <section>
    <div class="abs promo promo-1" role="img" aria-label="Photo of colourful printed cushions and plates">
      <div class="promo-card"><div class="promo-title">Sahel Grace</div><div class="promo-offer">For Sale</div><span class="promo-btn">BUY NOW</span></div>
    </div>
    <div class="abs promo promo-2" role="img" aria-label="Photo of a brown clay tea set">
      <div class="promo-card"><div class="promo-title">Sahel Grace</div><div class="promo-offer">25% Off</div><span class="promo-btn">BUY NOW</span></div>
    </div>
    <div class="abs promo promo-3" role="img" aria-label="Photo of a bright dining room with wooden table">
      <div class="promo-card"><div class="promo-title">Sahel Grace</div><div class="promo-offer">15 % Off</div><span class="promo-btn">BUY NOW</span></div>
    </div>
  </section>

  <footer>
    <div class="abs footer"></div>
    <div class="abs f-head newsletter">E-Mail Sign Up For Newsletter</div>
    <div class="abs signup">Enter Your E-mail Address<span class="signup-go">GO</span></div>
    <p class="abs blurb">Lorem Ipsum is simply dummy text of the printing and typesetting industry.</p>
    <div class="abs cards">
      <span style="width:45px">VANTA</span><span style="width:45px">AMBIX</span><span style="width:45px">MERCARD</span><span style="width:65px">PayWell</span>
    </div>

    <div class="abs col col-links"><div class="f-head">Our Links</div>
      <ul><li>Furniture</li><li>Decor</li><li>About us</li><li>Products</li><li>Upcoming sale</li><li>Faqs</li><li>Contact</li></ul>
    </div>
    <div class="abs col col-stories"><div class="f-head">Our Stories</div>
      <ul><li>Store Finder</li><li>New stores</li><li>Store events</li><li>Store services</li><li>Store Restaurants</li><li>Free personal shopper</li></ul>
    </div>
    <div class="abs col col-social"><div class="f-head">Connect With Us</div>
      <ul><li>Facelink<i></i></li><li>Chirper<i></i></li><li>Viewtube<i></i></li><li>Quorbit Plus<i></i></li><li>Workednet<i></i></li><li>RSS Feeds<i></i></li></ul>
    </div>
    <div class="abs copy">© 2014 Company Name ,All Rights Reserved</div>
  </footer>

</div>
</body>
</html>
```